Verosa Brow Studio

Start up business with a specialist in eye lash extensions

Target Market(s)

Woman if all ages

Industry/Entity Type

Beauty

Contact Information for Business Card

Image 1 is an example but the font needs to be easier read Front should have Mirela Koston in a stylish font with Lash extensions underneath . The front should have a stylish modern art picture of a woman eye and face on a faded pink. The back should have the same colour with her instigram QR and name , mobile +61488113264, instigam address , Verosa.brow.studio , Facebook: Verosa brow and st

Font styles to use
Sans Serif
Script

Colors
EB3D1F
EC4F4E
F09395
F8D3D4
FCEDEE

Requirements
Must have
• The name on front must be in clear stylist hand writing font

```html
<!DOCTYPE html>
<html lang="en">
<head>
<meta charset="utf-8">
<title>Verosa Brow Studio – Brand &amp; Business Cards</title>
<link href="https://fonts.googleapis.com/css2?family=Dancing+Script:wght@600&family=Montserrat:wght@300;400;500;600&display=swap" rel="stylesheet">
<style>
  :root {
    --red: #eb3d1f;
    --coral: #ec4f4e;
    --rose: #f09395;
    --blush: #f8d3d4;
    --mist: #fcedee;
    --wine: #8f2a1c;
  }
  * { margin: 0; padding: 0; box-sizing: border-box; }
  html, body { width: 1200px; height: 1200px; overflow: hidden; }
  body {
    position: relative;
    background: var(--mist);
    font-family: "Montserrat", sans-serif;
    color: var(--wine);
  }
  .brand-photo {
    position: absolute; left: 0; top: 0; width: 600px; height: 939px;
    background: linear-gradient(180deg, var(--blush) 0%, var(--rose) 40%, var(--coral) 62%, var(--rose) 82%, var(--blush) 100%);
  }
  .brand-band {
    position: absolute; left: 0; top: 939px; width: 600px; height: 261px;
    background: var(--red);
    color: var(--mist);
    text-align: center;
  }
  .brand-name {
    margin-top: 64px;
    font-family: "Dancing Script", cursive;
    font-weight: 600; font-size: 80px; line-height: 1;
  }
  .brand-tag {
    margin-top: 18px;
    font-weight: 400; font-size: 24px; letter-spacing: 6px; line-height: 1;
  }
  .stage { position: absolute; left: 600px; width: 600px; height: 600px; background: var(--mist); }
  .stage--front { top: 0; }
  .stage--back { top: 600px; }
  .card {
    position: absolute; left: 100px; top: 170px; width: 400px; height: 259px;
    background: var(--blush); border-radius: 18px;
  }
  .card-front { text-align: center; }
  .card-front .card-name {
    margin-top: 46px;
    font-family: "Dancing Script", cursive;
    font-weight: 600; font-size: 54px; line-height: 1; color: var(--red);
  }
  .card-front .card-tag {
    margin-top: 12px; font-size: 15px; font-weight: 500; letter-spacing: 4px; line-height: 1; color: var(--wine);
  }
  .card-front .services {
    margin-top: 34px; font-size: 11px; letter-spacing: 1px; line-height: 1.6; font-weight: 400; color: var(--wine);
  }
  .card-back .holder {
    position: absolute; left: 40px; top: 38px;
    font-family: "Dancing Script", cursive;
    font-weight: 600; font-size: 36px; line-height: 1; color: var(--red);
  }
  .card-back .role {
    position: absolute; left: 42px; top: 82px;
    font-size: 11px; font-weight: 500; letter-spacing: 3px; color: var(--wine);
  }
  .card-back .rule {
    position: absolute; left: 31px; top: 118px; width: 2px; height: 104px; background: var(--red);
  }
  .contact { position: absolute; left: 46px; top: 0; list-style: none; }
  .contact li {
    position: absolute; left: 0; width: 230px;
    display: flex; gap: 9px; font-size: 12px; font-weight: 500; line-height: 1.3; letter-spacing: .3px;
  }
  .contact svg { flex: none; width: 12px; height: 12px; margin-top: 2px; fill: var(--red); }
  .qr {
    position: absolute; right: 32px; top: 120px; width: 96px; height: 96px;
    background: var(--mist); border: 2px solid var(--red); border-radius: 6px;
  }
</style>
</head>
<body>
  <div class="brand-photo" role="img" aria-label="Stylish modern art portrait of a woman's eye and face on a faded pink background"></div>
  <section class="brand-band">
    <div class="brand-name">Mirela Koston</div>
    <div class="brand-tag">LASH EXTENSIONS</div>
  </section>

  <section class="stage stage--front">
    <div class="card card-front">
      <div class="card-name">Mirela Koston</div>
      <div class="card-tag">LASH EXTENSIONS</div>
      <div class="services">CLASSIC LASHES | 2D &amp; 3D LASHES<br>HOLIWOOD LASHES | LASH TINTING</div>
    </div>
  </section>

  <section class="stage stage--back">
    <div class="card card-back">
      <div class="holder">Mirela Koston</div>
      <div class="role">VEROSA BROW STUDIO</div>
      <div class="rule"></div>
      <ul class="contact">
        <li style="top:120px">
          <svg viewBox="0 0 24 24"><path d="M6.6 10.8a15.1 15.1 0 0 0 6.6 6.6l2.2-2.2c.3-.3.7-.4 1-.2 1.1.4 2.3.6 3.6.6.6 0 1 .4 1 1V20c0 .6-.4 1-1 1C10.6 21 3 13.4 3 4c0-.6.4-1 1-1h3.5c.6 0 1 .4 1 1 0 1.3.2 2.5.6 3.6.1.3 0 .7-.2 1z"/></svg>
          <span>+61 488 113 264</span>
        </li>
        <li style="top:147px">
          <svg viewBox="0 0 24 24"><circle cx="12" cy="12" r="8"/></svg>
          <span>Instagram: Verosa.brow.studio</span>
        </li>
        <li style="top:174px">
          <svg viewBox="0 0 24 24"><rect x="4" y="4" width="16" height="16"/></svg>
          <span>Facebook: Verosa brow and st</span>
        </li>
        <li style="top:201px">
          <svg viewBox="0 0 24 24"><path d="M2 5h20v14H2zM3.5 6.5 12 13l8.5-6.5v-.1h-17zm0 2.1V17.5l5.6-4.6zm17 0-5.6 4.3 5.6 4.6z"/></svg>
          <span>hello@verosastudio.com</span>
        </li>
      </ul>
      <div class="qr" role="img" aria-label="Instagram QR code area"></div>
    </div>
  </section>
</body>
</html>
```